Consulting company requires a logo and business card design

I require a logo/business card design for a new company based in Sexsmith Alberta called TallMeadow Field Advisory Ltd. I plan to provide the following services: Construction management/inspection for the oil and gas industry, as well as general consulting for Asset Management, fleet management, etc. Have attached a copy of resume for use as guide for

Target Market(s)

Businesses within the oil and gas production, construction and shipping industry

Industry/Entity Type

Oil And Gas

Contact Information for Business Card

Believe should highlight, services offered, safety, quality,

Logo Text

TallMeadow Field Advisory (TMFA) ?

Font styles to use
Script

Requirements
Must have
• Open to all options

```html
<!DOCTYPE html>
<html lang="en">
<head>
<meta charset="utf-8">
<title>TallMeadow Field Advisory Ltd – Business Card</title>
<link href="https://fonts.googleapis.com/css2?family=Lato:wght@400;700&display=swap" rel="stylesheet">
<style>
  :root {
    --stage: #000000;
    --paper: #ffffff;
    --gold: #f9b512;
    --sun-top: #ffd306;
    --sun-bottom: #fbb117;
    --swoosh: #f9a91c;
    --ink: #1a1a1a;
    --slate: #444444;
  }
  * { margin: 0; padding: 0; box-sizing: border-box; }
  html, body { width: 1200px; height: 900px; overflow: hidden; background: var(--stage); }
  body { position: relative; font-family: "Lato", sans-serif; }

  .card { position: absolute; top: 275px; width: 477px; height: 293px; overflow: hidden; }

  .card-front { left: 116px; background: var(--paper); border-radius: 0 56px 0 56px; color: var(--ink); }
  .holder { position: absolute; right: 19px; top: 34px; text-align: right; }
  .holder-name { font-size: 19px; font-weight: 700; color: var(--gold); line-height: 24px; }
  .holder-role { font-size: 13px; line-height: 16px; }

  .brand { position: absolute; left: 30px; top: 83px; color: var(--gold); font-weight: 400; }
  .brand-line { display: block; font-size: 28px; line-height: 32px; }
  .brand-tail { display: block; font-size: 22px; letter-spacing: 7px; line-height: 28px; }

  .address { position: absolute; right: 21px; top: 158px; text-align: right; font-size: 13px; line-height: 17px; }

  .contacts { position: absolute; right: 18px; top: 217px; list-style: none; font-size: 13px; line-height: 17.5px; }
  .contacts li { display: flex; justify-content: flex-end; align-items: center; gap: 7px; }
  .contacts svg { width: 11px; height: 11px; fill: var(--gold); }

  .card-back { left: 622px; top: 276px; height: 292px; border-radius: 56px 0 56px 0;
    background: linear-gradient(180deg, var(--sun-top) 0%, var(--sun-bottom) 100%); }
  .card-back .swoosh { position: absolute; inset: 0; width: 100%; height: 100%; }
  .back-brand { position: absolute; left: 0; right: 0; top: 166px; text-align: center; color: var(--paper); font-weight: 400; }
  .back-brand .brand-line { font-size: 38px; line-height: 44px; }
  .back-brand .brand-tail { font-size: 29px; letter-spacing: 10px; line-height: 36px; margin-left: 10px; }
</style>
</head>
<body>
  <section class="card card-front">
    <div class="holder">
      <p class="holder-name">Daniel Hartley</p>
      <p class="holder-role">Managing Director</p>
    </div>
    <div class="brand">
      <span class="brand-line">TallMeadow Field</span>
      <span class="brand-tail">Advisory Ltd</span>
    </div>
    <p class="address">4821, Meadow Ridge Road<br>Sexsmith, AB T0H 3C0</p>
    <ul class="contacts">
      <li>044-987 654 321
        <svg viewBox="0 0 24 24" aria-hidden="true"><path d="M6.6 10.8a15.1 15.1 0 0 0 6.6 6.6l2.2-2.2c.3-.3.7-.4 1-.2 1.1.4 2.3.6 3.6.6.6 0 1 .4 1 1V20c0 .6-.4 1-1 1A17 17 0 0 1 3 4c0-.6.4-1 1-1h3.5c.6 0 1 .4 1 1 0 1.3.2 2.5.6 3.6.1.3 0 .7-.2 1z"/></svg>
      </li>
      <li>info@tallmeadow.ca
        <svg viewBox="0 0 24 24" aria-hidden="true"><path d="M2 5h20v14H2zm2 2v.4l8 5 8-5V7z"/></svg>
      </li>
      <li>www.tallmeadow.ca
        <svg viewBox="0 0 24 24" aria-hidden="true"><path d="M10.6 13.4a1 1 0 0 1 0-1.4l3.5-3.5a1 1 0 1 1 1.4 1.4L12 13.4a1 1 0 0 1-1.4 0zM8 20a4 4 0 0 1-2.8-6.8l2.5-2.5 1.4 1.4-2.5 2.5a2 2 0 1 0 2.8 2.8l2.5-2.5 1.4 1.4-2.5 2.5A4 4 0 0 1 8 20zm8.3-6.7-1.4-1.4 2.5-2.5a2 2 0 1 0-2.8-2.8l-2.5 2.5-1.4-1.4 2.5-2.5a4 4 0 1 1 5.6 5.6z"/></svg>
      </li>
    </ul>
  </section>

  <section class="card card-back">
    <svg class="swoosh" viewBox="0 0 477 292" preserveAspectRatio="none" aria-hidden="true">
      <path d="M0 0 H88 C20 40 -10 150 60 250 C20 200 0 120 0 60 Z" fill="var(--swoosh)" opacity="0.75"/>
    </svg>
    <div class="back-brand">
      <span class="brand-line">TallMeadow Field</span>
      <span class="brand-tail">Advisory Ltd</span>
    </div>
  </section>
</body>
</html>
```